New Advertising Company Business Card

A two sided business card. One side with logo only and the other side with my information and maybe my logo again. Looking for something unique and creative, but not too busy. Info would include my name(Marcus Fenley), President, phone number, address, email address, and website. LOGO IS THE BLUE AND WHITE ONE.

Target Market(s)

CEO/VP Level Audience

Industry/Entity Type

Business

Contact Information for Business Card

In Description.

```html
<!DOCTYPE html>
<html lang="en">
<head>
<meta charset="utf-8">
<title>Lumen Advertising – Business Card</title>
<link href="https://fonts.googleapis.com/css2?family=Montserrat:wght@600;700&family=Open+Sans:wght@400&display=swap" rel="stylesheet">
<style>
  :root {
    --brand-blue: #1b75bc;
    --ink: #231f20;
    --text-grey: #5a5a5a;
    --paper: #ffffff;
    --backdrop: #f3f3f3;
  }
  html, body {
    margin: 0;
    padding: 0;
    width: 1200px;
    height: 1200px;
    overflow: hidden;
    background: var(--backdrop);
  }
  .canvas {
    position: relative;
    width: 1200px;
    height: 1200px;
  }
  .card {
    position: absolute;
    left: 170px;
    width: 870px;
    height: 486px;
    border-radius: 34px;
    overflow: hidden;
    box-shadow: 0 6px 14px rgba(0,0,0,0.18);
  }
  .card--front { top: 84px; background: var(--paper); }
  .card--back { top: 634px; background: var(--brand-blue); }

  .brand-name {
    position: absolute;
    margin: 0;
    font-family: "Montserrat", sans-serif;
    font-weight: 600;
    line-height: 1;
    text-align: center;
    white-space: nowrap;
  }
  .card--front .brand-name {
    left: 40px;
    width: 420px;
    top: 222px;
    font-size: 38px;
    color: var(--brand-blue);
  }
  .card--back .brand-name {
    left: 0;
    width: 870px;
    top: 206px;
    font-size: 54px;
    color: var(--paper);
  }

  .divider {
    position: absolute;
    left: 479px;
    top: 106px;
    width: 2px;
    height: 272px;
    background: var(--ink);
  }
  .contact {
    position: absolute;
    left: 520px;
    top: 100px;
    font-family: "Open Sans", sans-serif;
    color: var(--text-grey);
  }
  .contact__name {
    margin: 0;
    font-family: "Montserrat", sans-serif;
    font-weight: 700;
    font-size: 33px;
    color: var(--brand-blue);
    line-height: 1.1;
  }
  .contact__title { margin: 8px 0 0; font-size: 20px; }
  .contact__address { margin: 14px 0 0; font-size: 20px; line-height: 31px; }
  .contact__list { list-style: none; margin: 16px 0 0; padding: 0; font-size: 20px; line-height: 31px; }
  .contact__list li { display: flex; align-items: center; }
  .contact__list svg { width: 18px; height: 18px; margin-right: 10px; fill: var(--brand-blue); flex: none; }

  .footer-rule {
    position: absolute;
    left: 0;
    width: 870px;
    top: 424px;
    height: 5px;
    background: var(--ink);
  }
  .footer-band {
    position: absolute;
    left: 0;
    width: 870px;
    top: 434px;
    bottom: 0;
    background: var(--brand-blue);
  }

  .back-url {
    position: absolute;
    left: 0;
    width: 870px;
    top: 430px;
    text-align: center;
    font-family: "Open Sans", sans-serif;
    font-size: 19px;
    color: var(--paper);
  }
</style>
</head>
<body>
<div class="canvas">

  <section class="card card--front" aria-label="Business card front">
    <p class="brand-name">Lumen Advertising</p>
    <div class="divider"></div>
    <div class="contact">
      <h1 class="contact__name">Marcus Fenley</h1>
      <p class="contact__title">President</p>
      <p class="contact__address">Street Name Avenue, Suite<br>100 State, Zip Code,Country</p>
      <ul class="contact__list">
        <li><svg viewBox="0 0 24 24"><path d="M6.6 10.8a15.1 15.1 0 0 0 6.6 6.6l2.2-2.2c.3-.3.7-.4 1-.2 1.1.4 2.3.6 3.6.6.6 0 1 .4 1 1V20c0 .6-.4 1-1 1A17 17 0 0 1 3 4c0-.6.4-1 1-1h3.5c.6 0 1 .4 1 1 0 1.300.2 2.500.6 3.600.1.300 0 .700-.2 1z"/></svg>+000.000.00 00</li>
        <li><svg viewBox="0 0 24 24"><path d="M7 1h10a2 2 0 0 1 2 2v18a2 2 0 0 1-2 2H7a2 2 0 0 1-2-2V3a2 2 0 0 1 2-2zm0 3v14h10V4zm5 15.2a1.2 1.2 0 1 0 0 2.4 1.2 1.2 0 0 0 0-2.4z"/></svg>+000.000.00 00</li>
        <li><svg viewBox="0 0 24 24"><path d="M2 5h20v14H2zm2 2v.4l8 5.2 8-5.2V7l-8 5.2z"/></svg>info@yourmailaddress.com</li>
        <li><svg viewBox="0 0 24 24"><path d="M12 2a10 10 0 1 0 0 20 10 10 0 0 0 0-20zm0 2a8 8 0 0 1 0 16 8 8 0 0 1 0-16zM3 11h18v2H3zm8-8h2v18h-2z"/></svg>www.yourmailaddress.com</li>
      </ul>
    </div>
    <div class="footer-rule"></div>
    <div class="footer-band"></div>
  </section>

  <section class="card card--back" aria-label="Business card back">
    <p class="brand-name">Lumen Advertising</p>
    <div class="back-url">www.yourmailaddress.com</div>
  </section>

</div>
</body>
</html>
```